Design ecommerce website for www.velmorissa.com

Design a Website given below details
Name - www.velmorissa.com

Given a shopify theme :Brightcart
http://layoutbazaar.net/item/brightcart-responsive-shopify-theme/4817203

Given type of products that will be sold
http://tarokbars.pelisite.com
Wendlomart.in
( above designs are not good )

Given competitors
www.zorbelle.com ( especially like how each category is sold as a story )
www.gindova.com

Given Tg
Women 20 +
Aspirational

Website has to be fresh peppy and understated sexy

No need to push Organic agenda too much but it is present in background story

Let me know if any more info required
Updates

Reason: Look for forward to revised designs / new designs

Target Market(s)

Women
20 +
Primarily Indian
Aspirational

Industry/Entity Type

Hair And Beauty

Number of Pages Required

5+ page

Font styles to use
Sans Serif

Requirements
Must have
• Hi Quality Images ( i will provide images )
• Good fun icons
• Good font
• Peppy / classy color scheme
• THe main focus is on the main page / landing page. Need a design which is intuitive and lends itself well to beauty products. Creating an exclusive experiance for women
• The other pages are
• Modified page for product categories ( eg page for all Skin products )
• Modified page for each product
• About page / Check out page
• These are essentially modifications to main page with minor alterations
• Important to remember that we are building using the Brightcart Shopify theme.
• If you recommend shopify apps, I would purchase those too.
Nice to have
• Disctintive fonts.
• Usage of elements/ fonts / icons which make the site very quirky and fun
• I am open to suggestions to changes in words or using images instead of words to convey information
Should not have
• Too much of green / organic feel
• Too much artificial feel ( no neons )

```html
<!DOCTYPE html>
<html lang="en">
<head>
<meta charset="utf-8">
<title>Velmorissa — Natural Beauty Store</title>
<link href="https://fonts.googleapis.com/css2?family=Oswald:wght@300;400;500&family=Open+Sans:wght@400;600;700&display=swap" rel="stylesheet">
<style>
:root{
  --blue:#2aa6df;
  --blue-dark:#1b86bf;
  --green:#8cc63e;
  --green-dark:#6fa52a;
  --ink:#333333;
  --muted:#777777;
  --header:#2b2b2b;
  --footer:#2f2f2f;
  --footer-bar:#1f1f1f;
  --paper:#ffffff;
  --mist:#eef0f1;
  --line:#dcdcdc;
  --red:#d8262b;
  --star:#f2b01e;
}
*{box-sizing:border-box;margin:0;padding:0}
html,body{width:1200px;height:2984px;overflow:hidden}
body{position:relative;background:var(--paper);font-family:"Open Sans",Arial,sans-serif;color:var(--ink)}
.abs{position:absolute}
.heading{font-family:"Oswald",Arial,sans-serif;font-weight:400;text-transform:uppercase;letter-spacing:.5px}
.photo{position:absolute}

/* promo banner */
.promo{left:0;top:0;width:1200px;height:108px;background:linear-gradient(90deg,#f4f6f7,#ffffff 45%,#eef6f2)}
.promo-title{left:500px;top:8px;font-weight:600;font-size:36px;color:var(--blue-dark);white-space:nowrap}
.promo-sub{left:500px;top:56px;font-weight:600;font-size:28px;color:#555;white-space:nowrap}
.promo-btn{left:930px;top:6px;width:140px;height:40px;background:var(--green);color:#fff;font-weight:700;font-size:18px;text-align:center;line-height:40px;border-radius:4px}

/* header */
.header{left:0;top:108px;width:1200px;height:140px;background:var(--header)}
.logo{left:72px;top:40px;display:flex;align-items:center;gap:12px}
.logo-mark{width:34px;height:34px;border-radius:50%;background:var(--green)}
.logo-name{font-weight:600;font-size:34px;color:var(--green)}
.toplinks{right:120px;top:18px;display:flex;gap:28px;font-size:15px;color:#ddd}
.toplinks span{display:flex;align-items:center;gap:6px}
.toplinks svg{width:14px;height:14px}
.nav{left:520px;top:76px;display:flex;font-size:18px;color:#eee;white-space:nowrap}
.nav span{padding:6px 20px}
.nav .on{background:var(--blue);color:#fff}
.nav .offer{color:var(--green)}

/* hero */
.hero{left:0;top:248px;width:1200px;height:472px;background:linear-gradient(90deg,#e9d3c8 0%,#e2e3e4 40%,#d8dadb 100%)}
.hero-face{left:0;top:0;width:330px;height:472px;background:linear-gradient(160deg,#f1d7c9,#d9ad96)}
.hero-products{left:300px;top:70px;width:440px;height:380px;background:linear-gradient(180deg,#c8cacc,#e8e9ea)}
.hero-card{left:760px;top:80px;width:360px;height:320px;background:rgba(255,255,255,.92);padding:30px 0 0 26px}
.hero-line{display:inline-block;font-family:"Oswald",sans-serif;font-weight:400;font-size:29px;text-transform:uppercase;color:#333;padding:2px 10px;margin-bottom:8px;line-height:1.2;white-space:nowrap}
.hero-line.hl{background:var(--green);color:#fff}
.hero-btn{position:absolute;left:80px;top:230px;width:200px;height:50px;border:2px solid var(--blue);color:var(--blue);font-size:22px;text-align:center;line-height:46px;background:#fff}
.dots{left:560px;top:436px;display:flex;gap:10px}
.dots i{width:14px;height:14px;border-radius:50%;border:2px solid #555;background:#fff}
.dots i.on{background:#555}

/* caption strip */
.caption{left:0;top:720px;width:1200px;height:140px;background:linear-gradient(180deg,#f3f3f3,#ffffff)}
.caption-text{left:0;top:18px;width:1200px;text-align:center;font-size:22px;color:#555}
.caption-btn{left:500px;top:66px;width:200px;height:50px;border:2px solid var(--blue);color:var(--blue);font-size:22px;text-align:center;line-height:46px}

/* story tiles */
.tile{top:930px;width:322px;height:240px;overflow:hidden}
.tile-label{position:absolute;font-family:"Oswald",sans-serif;text-transform:uppercase;color:#333;white-space:nowrap}
.t1{left:72px;background:linear-gradient(180deg,#7cc6e8,#bfe3ef 55%,#e8d8b4)}
.t2{left:440px;background:linear-gradient(90deg,#ece7e2,#c9a58d)}
.t3{left:808px;background:linear-gradient(135deg,#e7c0b4,#b5897e)}
.t1 .tile-label{left:20px;top:18px;font-size:30px;background:#fff;padding:0 10px}
.t2 .tile-label{left:18px;top:70px;font-size:30px;line-height:1.25;color:#444}
.t3 .tile-label{left:24px;bottom:18px;font-size:30px;background:rgba(255,255,255,.85);padding:0 14px}

/* recipe bar */
.recipe{left:0;top:1186px;width:1200px;height:140px;background:linear-gradient(180deg,#ffffff,#eef0f1)}
.recipe-face{left:10px;top:6px;width:170px;height:134px;background:linear-gradient(160deg,#d9b49d,#8a5a44)}
.recipe-text{left:270px;top:52px;font-size:32px;color:var(--blue);white-space:nowrap}
.recipe-btn{left:770px;top:50px;width:150px;height:46px;background:var(--blue);color:#fff;font-size:20px;font-weight:600;text-align:center;line-height:46px;border-radius:3px}
.recipe-herbs{left:930px;top:20px;width:270px;height:120px;background:linear-gradient(90deg,#f3d9a7,#c7783f)}

/* game + quiz */
.game{left:0;top:1340px;width:600px;height:620px;background:linear-gradient(180deg,#f4f5f6,#e6e8e9)}
.quiz{left:600px;top:1340px;width:600px;height:620px;background:linear-gradient(180deg,#fafafa,#eceeef);border-left:1px solid var(--line)}
.sec-title{font-family:"Oswald",sans-serif;font-weight:400;text-transform:uppercase;color:var(--green);font-size:32px;line-height:1.3;white-space:nowrap}
.game .sec-title{left:30px;top:28px}
.game-btn{left:40px;width:320px;height:78px;background:linear-gradient(180deg,#3db5ea,var(--blue-dark));border-radius:40px;color:#fff;font-size:32px;line-height:78px;padding-left:110px}
.game-icon{position:absolute;left:-6px;top:-6px;width:90px;height:90px;border-radius:50%;background:#fff;border:3px solid #cfe9f6}
.game-icon i{position:absolute;left:12px;top:12px;width:60px;height:60px;border-radius:50%;background:linear-gradient(160deg,#f2c28a,#d36f6f)}
.play-btn{left:260px;top:468px;width:84px;height:40px;background:var(--green);color:#222;font-weight:600;font-size:18px;text-align:center;line-height:40px;border-radius:3px}
.quiz .sec-title{left:40px;top:28px}
.q-label{left:52px;top:150px;font-weight:700;font-size:18px;color:#333}
.q-rule{left:40px;top:178px;width:520px;height:1px;background:var(--line)}
.q-text{left:52px;top:190px;width:300px;font-size:17px;line-height:1.5;color:#444}
.next-btn{left:52px;top:300px;width:110px;height:46px;background:var(--green);color:#222;font-weight:700;font-size:20px;text-align:center;line-height:46px;border-radius:3px}
.stamp{left:380px;top:250px;width:170px;height:170px;border-radius:50%;background:radial-gradient(circle,#e8555a,#c81f25)}

/* products */
.shelf-title{left:0;top:2016px;width:1200px;text-align:center;color:var(--green);font-size:36px}
.shelf-rule{left:520px;top:2072px;width:160px;height:2px;background:var(--green)}
.card{top:2096px;width:240px;height:296px;background:#fff;border:1px solid var(--line);box-shadow:0 2px 4px rgba(0,0,0,.08)}
.card-img{position:absolute;left:20px;top:14px;width:200px;height:140px}
.card-title{position:absolute;left:0;top:170px;width:100%;text-align:center;font-size:13px;font-weight:700;color:var(--green);text-transform:uppercase}
.stars{position:absolute;left:0;top:190px;width:100%;display:flex;justify-content:center;gap:2px}
.stars svg{width:14px;height:14px}
.price{position:absolute;left:0;top:214px;width:100%;text-align:center;font-size:22px;font-weight:600;color:#333}
.card-actions{position:absolute;left:0;bottom:0;width:100%;height:40px;border-top:1px solid var(--line);display:flex;justify-content:space-around;align-items:center;font-size:12px;color:#555;white-space:nowrap}
.c1{left:72px}.c2{left:352px}.c3{left:632px}.c4{left:912px}

/* testimonial */
.testimonial{left:0;top:2400px;width:1200px;height:320px;background:var(--mist)}
.testi-title{left:0;top:40px;width:1200px;text-align:center;font-size:38px;color:var(--blue);font-weight:300}
.testi-rule{left:460px;top:98px;width:280px;height:2px;background:var(--blue)}
.testi-dot{left:592px;top:92px;width:16px;height:16px;border-radius:50%;background:var(--blue)}
.testi-text{left:200px;top:128px;width:800px;text-align:center;font-size:15px;line-height:1.7;color:#555}
.testi-name{left:0;top:222px;width:1200px;text-align:center;font-size:15px;color:var(--blue)}
.arrow{top:150px;width:30px;height:50px}

/* footer */
.footer{left:0;top:2720px;width:1200px;height:200px;background:var(--footer);color:#ddd}
.care{left:80px;top:56px;display:flex;gap:16px;align-items:center}
.care-icon{width:54px;height:54px;border-radius:50%;border:2px solid #bbb;display:flex;align-items:center;justify-content:center}
.care-text{font-size:16px;line-height:1.5;white-space:nowrap}
.news{left:460px;top:50px;font-size:16px}
.news-field{margin-top:8px;width:270px;height:36px;border:1px solid #777;background:#3a3a3a;color:#999;font-size:14px;line-height:34px;padding-left:10px;position:relative}
.news-field b{position:absolute;right:6px;top:7px;width:20px;height:20px;border:1px solid #999}
.social{left:820px;top:48px;font-size:16px}
.social-row{display:flex;gap:10px;margin-top:8px}
.social-row i{width:40px;height:40px;border-radius:50%;background:var(--blue)}
.legal{left:0;top:2920px;width:1200px;height:64px;background:var(--footer-bar)}
.legal-links{left:0;top:10px;width:1200px;display:flex;justify-content:center;gap:70px;font-size:14px;color:#ccc;text-transform:uppercase}
.legal-links .on{color:var(--green)}
.copy{left:0;top:38px;width:1200px;text-align:center;font-size:13px;color:#999}
</style>
</head>
<body>

<!-- promo banner -->
<div class="abs promo">
  <div class="photo" style="left:0;top:0;width:120px;height:108px;background:linear-gradient(160deg,#e9b59a,#a8523d)" role="img" aria-label="Photo of a model with red hair"></div>
  <div class="photo" style="left:130px;top:6px;width:340px;height:96px;background:linear-gradient(90deg,#d7d9dc,#f0f0f0)" role="img" aria-label="Row of makeup brushes and cosmetics"></div>
  <div class="abs promo-title">Natural Product</div>
  <div class="abs promo-sub">Up to 15% off</div>
  <div class="abs promo-btn">SHOP NOW</div>
  <div class="photo" style="left:900px;top:52px;width:300px;height:56px;background:linear-gradient(90deg,#cfe9c4,#9fd27e)" role="img" aria-label="Cucumber slices and natural ingredients"></div>
</div>

<!-- header -->
<header class="abs header">
  <div class="abs logo"><span class="logo-mark"></span><span class="logo-name">Velmorissa</span></div>
  <div class="abs toplinks">
    <span><svg viewBox="0 0 14 14"><circle cx="7" cy="4.5" r="3" fill="var(--blue)"/><path d="M1 14c0-4 3-6 6-6s6 2 6 6z" fill="var(--blue)"/></svg>Account</span>
    <span><svg viewBox="0 0 14 14"><rect x="1" y="3" width="12" height="8" fill="none" stroke="#ddd" stroke-width="1.4"/><path d="M1 3l6 5 6-5" fill="none" stroke="#ddd" stroke-width="1.4"/></svg>Contact us</span>
    <span><svg viewBox="0 0 14 14"><path d="M1 2h2l2 8h7l1-6H4" fill="none" stroke="#ddd" stroke-width="1.4"/><circle cx="6" cy="12.5" r="1.2" fill="#ddd"/><circle cx="11" cy="12.5" r="1.2" fill="#ddd"/></svg>My Cart</span>
  </div>
  <nav class="abs nav">
    <span class="on">Skin</span><span>Hair</span><span>Make Up</span><span>Bath and Body</span><span class="offer">Offer zone</span>
  </nav>
</header>

<!-- hero -->
<section class="abs hero">
  <div class="photo hero-face" role="img" aria-label="Close-up of a model applying lipstick with red nails"></div>
  <div class="photo hero-products" role="img" aria-label="Skincare tubes and a lipstick arranged as a product group"></div>
  <div class="abs hero-card">
    <span class="hero-line">Login for</span><br>
    <span class="hero-line hl">Customised offers and</span><br>
    <span class="hero-line hl">Recommendations</span>
    <div class="hero-btn">Shop Now »</div>
  </div>
  <div class="abs dots"><i class="on"></i><i></i><i></i><i></i><i></i></div>
</section>

<!-- caption -->
<section class="abs caption">
  <div class="abs caption-text">Catch the Season's Best Recommendations, Trial packs, Offers, and personalized advice</div>
  <div class="abs caption-btn">Login Now »</div>
</section>

<!-- story tiles -->
<div class="abs tile t1" role="img" aria-label="Beach scene with sunscreen and beauty products"><span class="tile-label">Our top 10 brands</span></div>
<div class="abs tile t2" role="img" aria-label="Portrait of a model with flowing hair"><span class="tile-label">Natural<br>Beauty<br>Secrets</span></div>
<div class="abs tile t3" role="img" aria-label="Makeup artist applying makeup to a model"><span class="tile-label">Ask the expert</span></div>

<!-- recipe bar -->
<section class="abs recipe">
  <div class="photo recipe-face" role="img" aria-label="Model with long dark hair"></div>
  <div class="abs recipe-text heading">Submit your natural beauty recipe</div>
  <div class="abs recipe-btn">Submit »</div>
  <div class="photo recipe-herbs" role="img" aria-label="Bowls of honey, powders and flowers"></div>
</section>

<!-- game -->
<section class="abs game">
  <h2 class="abs sec-title">Play the natural beauty game</h2>
  <div class="abs game-btn" style="top:108px"><span class="game-icon"><i></i></span>Make Up</div>
  <div class="abs game-btn" style="top:240px"><span class="game-icon"><i></i></span>Dress Up</div>
  <div class="abs game-btn" style="top:372px"><span class="game-icon"><i></i></span>Facial</div>
  <div class="abs play-btn">Play »</div>
</section>

<!-- quiz -->
<section class="abs quiz">
  <h2 class="abs sec-title">Answer three questions and<br>get a special discount code</h2>
  <div class="abs q-label">Question</div>
  <div class="abs q-rule"></div>
  <div class="abs q-text">1.) Lorem Ipsum is simply dummy text of the printing and typesetting industry?</div>
  <div class="abs next-btn">Next »</div>
  <div class="abs stamp" role="img" aria-label="Round red discount stamp badge"></div>
</section>

<!-- products -->
<h2 class="abs shelf-title heading">Naturally Nice</h2>
<div class="abs shelf-rule"></div>

<article class="abs card c1">
  <div class="card-img" style="background:linear-gradient(135deg,#d9efc4,#7fb24d)" role="img" aria-label="Green soap bar product"></div>
  <div class="card-title">Product Title</div>
  <div class="stars"><svg viewBox="0 0 10 10"><path d="M5 0l1.5 3.2 3.5.4-2.6 2.4.7 3.5L5 7.8 1.9 9.5l.7-3.5L0 3.6l3.5-.4z" fill="var(--star)"/></svg><svg viewBox="0 0 10 10"><path d="M5 0l1.5 3.2 3.5.4-2.6 2.4.7 3.5L5 7.8 1.9 9.5l.7-3.5L0 3.6l3.5-.4z" fill="var(--star)"/></svg><svg viewBox="0 0 10 10"><path d="M5 0l1.5 3.2 3.5.4-2.6 2.4.7 3.5L5 7.8 1.9 9.5l.7-3.5L0 3.6l3.5-.4z" fill="var(--star)"/></svg><svg viewBox="0 0 10 10"><path d="M5 0l1.5 3.2 3.5.4-2.6 2.4.7 3.5L5 7.8 1.9 9.5l.7-3.5L0 3.6l3.5-.4z" fill="var(--star)"/></svg><svg viewBox="0 0 10 10"><path d="M5 0l1.5 3.2 3.5.4-2.6 2.4.7 3.5L5 7.8 1.9 9.5l.7-3.5L0 3.6l3.5-.4z" fill="#ccc"/></svg></div>
  <div class="price">$ 50.00</div>
  <div class="card-actions"><span>☰ Select Option</span><span>♡ Add to Wishlist</span></div>
</article>

<article class="abs card c2">
  <div class="card-img" style="background:linear-gradient(135deg,#f3e6d3,#c9a27c)" role="img" aria-label="Open powder compact product"></div>
  <div class="card-title">Product Title</div>
  <div class="stars"><svg viewBox="0 0 10 10"><path d="M5 0l1.5 3.2 3.5.4-2.6 2.4.7 3.5L5 7.8 1.9 9.5l.7-3.5L0 3.6l3.5-.4z" fill="var(--star)"/></svg><svg viewBox="0 0 10 10"><path d="M5 0l1.5 3.2 3.5.4-2.6 2.4.7 3.5L5 7.8 1.9 9.5l.7-3.5L0 3.6l3.5-.4z" fill="var(--star)"/></svg><svg viewBox="0 0 10 10"><path d="M5 0l1.5 3.2 3.5.4-2.6 2.4.7 3.5L5 7.8 1.9 9.5l.7-3.5L0 3.6l3.5-.4z" fill="var(--star)"/></svg><svg viewBox="0 0 10 10"><path d="M5 0l1.5 3.2 3.5.4-2.6 2.4.7 3.5L5 7.8 1.9 9.5l.7-3.5L0 3.6l3.5-.4z" fill="var(--star)"/></svg><svg viewBox="0 0 10 10"><path d="M5 0l1.5 3.2 3.5.4-2.6 2.4.7 3.5L5 7.8 1.9 9.5l.7-3.5L0 3.6l3.5-.4z" fill="#ccc"/></svg></div>
  <div class="price">$ 50.00</div>
  <div class="card-actions"><span>☰ Select Option</span><span>♡ Add to Wishlist</span></div>
</article>

<article class="abs card c3">
  <div class="card-img" style="background:linear-gradient(135deg,#f4f4f4,#b3222c)" role="img" aria-label="Red lipstick product"></div>
  <div class="card-title">Product Title</div>
  <div class="stars"><svg viewBox="0 0 10 10"><path d="M5 0l1.5 3.2 3.5.4-2.6 2.4.7 3.5L5 7.8 1.9 9.5l.7-3.5L0 3.6l3.5-.4z" fill="var(--star)"/></svg><svg viewBox="0 0 10 10"><path d="M5 0l1.5 3.2 3.5.4-2.6 2.4.7 3.5L5 7.8 1.9 9.5l.7-3.5L0 3.6l3.5-.4z" fill="var(--star)"/></svg><svg viewBox="0 0 10 10"><path d="M5 0l1.5 3.2 3.5.4-2.6 2.4.7 3.5L5 7.8 1.9 9.5l.7-3.5L0 3.6l3.5-.4z" fill="var(--star)"/></svg><svg viewBox="0 0 10 10"><path d="M5 0l1.5 3.2 3.5.4-2.6 2.4.7 3.5L5 7.8 1.9 9.5l.7-3.5L0 3.6l3.5-.4z" fill="var(--star)"/></svg><svg viewBox="0 0 10 10"><path d="M5 0l1.5 3.2 3.5.4-2.6 2.4.7 3.5L5 7.8 1.9 9.5l.7-3.5L0 3.6l3.5-.4z" fill="#ccc"/></svg></div>
  <div class="price">$ 50.00</div>
  <div class="card-actions"><span>☰ Select Option</span><span>♡ Add to Wishlist</span></div>
</article>

<article class="abs card c4">
  <div class="card-img" style="background:linear-gradient(135deg,#f7ece6,#d8a18d)" role="img" aria-label="Tube of tinted cream"></div>
  <div class="card-title">Product Title</div>
  <div class="stars"><svg viewBox="0 0 10 10"><path d="M5 0l1.5 3.2 3.5.4-2.6 2.4.7 3.5L5 7.8 1.9 9.5l.7-3.5L0 3.6l3.5-.4z" fill="var(--star)"/></svg><svg viewBox="0 0 10 10"><path d="M5 0l1.5 3.2 3.5.4-2.6 2.4.7 3.5L5 7.8 1.9 9.5l.7-3.5L0 3.6l3.5-.4z" fill="var(--star)"/></svg><svg viewBox="0 0 10 10"><path d="M5 0l1.5 3.2 3.5.4-2.6 2.4.7 3.5L5 7.8 1.9 9.5l.7-3.5L0 3.6l3.5-.4z" fill="var(--star)"/></svg><svg viewBox="0 0 10 10"><path d="M5 0l1.5 3.2 3.5.4-2.6 2.4.7 3.5L5 7.8 1.9 9.5l.7-3.5L0 3.6l3.5-.4z" fill="var(--star)"/></svg><svg viewBox="0 0 10 10"><path d="M5 0l1.5 3.2 3.5.4-2.6 2.4.7 3.5L5 7.8 1.9 9.5l.7-3.5L0 3.6l3.5-.4z" fill="#ccc"/></svg></div>
  <div class="price">$ 50.00</div>
  <div class="card-actions"><span>☰ Select Option</span><span>♡ Add to Wishlist</span></div>
</article>

<!-- testimonial -->
<section class="abs testimonial">
  <h2 class="abs testi-title heading">Testimonial</h2>
  <div class="abs testi-rule"></div>
  <div class="abs testi-dot"></div>
  <p class="abs testi-text">Lorem Ipsum is simply dummy text of the printing and typesetting industry. Lorem Ipsum has been the industry's standard dummy text ever since the 1500s, when an unknown printer took a galley.</p>
  <div class="abs testi-name">- Client name</div>
  <svg class="abs arrow" style="left:110px" viewBox="0 0 30 50"><path d="M24 4L6 25l18 21" fill="none" stroke="#444" stroke-width="4"/></svg>
  <svg class="abs arrow" style="left:1060px" viewBox="0 0 30 50"><path d="M6 4l18 21L6 46" fill="none" stroke="#444" stroke-width="4"/></svg>
</section>

<!-- footer -->
<footer class="abs footer">
  <div class="abs care">
    <div class="care-icon"><svg width="24" height="24" viewBox="0 0 24 24"><path d="M6 2l4 4-2 3c1.5 3 4 5.5 7 7l3-2 4 4-3 4C10 21 3 14 2 5z" fill="#ccc"/></svg></div>
    <div class="care-text">Customer Care 040 3187 2650<br>Mon - Sun 10AM to 7PM</div>
  </div>
  <div class="abs news">Get special discounts on your inbox
    <div class="news-field">Enter your email id<b></b></div>
  </div>
  <div class="abs social">Connect With us
    <div class="social-row"><i></i><i></i><i></i><i></i><i></i></div>
  </div>
</footer>
<div class="abs legal">
  <div class="abs legal-links"><span class="on">Terms and Condition</span><span>Privacy Policy</span><span>Shipping Policy</span><span>Cancellation and Return Policy</span></div>
  <div class="abs copy">© Velmorissa - 2015. All rights reserved</div>
</div>

</body>
</html>
```